Valdora Business Card Design - Professional Flexible and forward thinking. Clean and Easy to follow

Management Consulting Company. I focus on business development and concept and operational review. I need a progressive, simple and professional layout design for the business cards, letterhead and envelops
Professional Flexible and forward thinking. Clean and Easy to follow
Mature Business persons and professionals and Corporations

Target Market(s)

Mature Business persons and professionals and Corporations - Government org.

Industry/Entity Type

Consulting

Contact Information for Business Card

Requirements
Must have
• Marcus Valdora
• President
• Phone - 555.382.6047
• email - Mvaldora@valdorapartners.com
• Skype - Marc.valdora
• 7215 Pellham Avenue
• Suite 4B
• Linden Harbor, N.Y. 11592
• USA
Nice to have
• www.valdorapartners.com
Should not have
• N/A

```html
<!DOCTYPE html>
<html lang="en">
<head>
<meta charset="utf-8">
<title>Valdora Partners Stationery</title>
<link href="https://fonts.googleapis.com/css2?family=Fira+Sans:wght@400;500&display=swap" rel="stylesheet">
<style>
  :root {
    --brand-blue: #1d52a3;
    --brand-blue-deep: #1a4796;
    --brand-blue-light: #2a7fd4;
    --paper: #ffffff;
    --backdrop: #ebebeb;
    --ink: #3a3a3a;
    --title-grey: #58595b;
    --shadow: 0 2px 6px rgba(0,0,0,0.12);
  }
  * { box-sizing: border-box; margin: 0; padding: 0; }
  html, body { width: 1200px; height: 1200px; overflow: hidden; }
  body {
    background: var(--backdrop);
    font-family: "Fira Sans", sans-serif;
    color: var(--ink);
    position: relative;
  }
  .sheet { position: absolute; background: var(--paper); box-shadow: var(--shadow); }

  /* Letterhead */
  .letterhead { left: 60px; top: 110px; width: 470px; height: 640px; }
  .letterhead .side-band { position: absolute; left: 0; top: 0; bottom: 0; width: 26px; background: var(--brand-blue); }
  .contact-list { list-style: none; position: absolute; left: 8px; bottom: 22px; font-size: 11.5px; line-height: 1.35; }
  .contact-list li { display: flex; align-items: flex-start; gap: 12px; }
  .contact-list .icon { width: 10px; height: 10px; margin-top: 3px; flex: none; }
  .contact-list .icon.blank { visibility: hidden; }

  /* Envelope front */
  .envelope-front { left: 580px; top: 110px; width: 460px; height: 230px; }
  .envelope-front .side-band { position: absolute; left: 0; top: 0; bottom: 0; width: 22px; background: var(--brand-blue); }
  .return-address { position: absolute; left: 6px; bottom: 18px; display: flex; gap: 10px; font-size: 10.5px; line-height: 1.3; align-items: center; }

  /* Envelope back */
  .envelope-back { left: 580px; top: 370px; width: 460px; height: 240px; overflow: hidden; }
  .envelope-back .flap { position: absolute; left: 0; right: 0; top: 0; height: 56px; background: var(--brand-blue-deep); border-radius: 0 0 22px 22px; }

  /* Business cards */
  .card { position: absolute; width: 260px; height: 150px; box-shadow: var(--shadow); top: 650px; }
  .card-front { left: 580px; background: var(--paper); display: flex; }
  .card-front .identity { width: 42%; display: flex; flex-direction: column; align-items: center; justify-content: center; gap: 4px; }
  .brand-mark { display: flex; align-items: center; gap: 5px; font-size: 15px; color: var(--brand-blue); font-weight: 500; }
  .brand-mark .square { width: 12px; height: 12px; background: var(--brand-blue); }
  .person-name { font-size: 10px; color: var(--brand-blue-light); font-weight: 500; margin-top: 4px; }
  .person-role { font-size: 7px; color: var(--brand-blue-light); }
  .card-front .details { flex: 1; background: linear-gradient(135deg, var(--brand-blue-light), var(--brand-blue)); border-left: 3px solid #4aa3e8; color: #fff; font-size: 6.5px; line-height: 1.4; padding: 14px 8px; display: flex; flex-direction: column; justify-content: space-between; }
  .card-front .details p { display: flex; gap: 4px; }
  .card-front .details .dot { width: 5px; height: 5px; border: 1px solid #fff; margin-top: 2px; flex: none; }
  .card-back { left: 870px; background: radial-gradient(circle at 55% 35%, #2a64c0, var(--brand-blue-deep)); display: flex; align-items: center; justify-content: center; }
  .card-back .brand-mark { color: #fff; font-size: 22px; }
  .card-back .brand-mark .square { background: #fff; width: 16px; height: 16px; }

  /* Presentation title */
  .presentation-title { position: absolute; right: 85px; top: 1058px; font-size: 72px; font-weight: 500; letter-spacing: 2px; color: var(--title-grey); }
</style>
</head>
<body>

<section class="sheet letterhead" aria-label="Letterhead">
  <div class="side-band"></div>
  <ul class="contact-list">
    <li><svg class="icon" viewBox="0 0 10 10"><rect width="10" height="10" fill="#3d8fe0"/><circle cx="5" cy="5" r="2.5" fill="#fff"/></svg>Marc.valdora</li>
    <li><svg class="icon" viewBox="0 0 10 10"><rect width="10" height="10" fill="#fff"/><path d="M3 2h2v2l-1 1 1 1.5 1-1h2v2H6C4 7.5 2.5 6 2.5 4V2z" fill="var(--brand-blue)"/></svg>555.382.6047</li>
    <li><svg class="icon" viewBox="0 0 10 10"><rect width="10" height="10" fill="#fff"/><path d="M5 1.5C3.3 1.5 2.3 2.7 2.3 4c0 2 2.7 4.5 2.7 4.5S7.7 6 7.7 4c0-1.3-1-2.5-2.7-2.5z" fill="var(--brand-blue)"/></svg>7215 Pellham Avenue</li>
    <li><span class="icon blank"></span>Suite 4B, Linden Harbor</li>
    <li><span class="icon blank"></span>N.Y. 11592, USA</li>
    <li><svg class="icon" viewBox="0 0 10 10"><rect width="10" height="10" fill="#fff"/><circle cx="5" cy="5" r="3.3" fill="none" stroke="var(--brand-blue)"/><path d="M1.7 5h6.6M5 1.7v6.6" stroke="var(--brand-blue)" stroke-width=".7"/></svg>www.valdorapartners.com</li>
    <li><svg class="icon" viewBox="0 0 10 10"><rect width="10" height="10" fill="#fff"/><rect x="1.5" y="2.5" width="7" height="5" fill="var(--brand-blue)"/><path d="M1.5 2.5 5 5.5 8.5 2.5" stroke="#fff" stroke-width=".7" fill="none"/></svg>Mvaldora@valdorapartners.com</li>
  </ul>
</section>

<section class="sheet envelope-front" aria-label="Envelope front">
  <div class="side-band"></div>
  <div class="return-address">
    <svg width="10" height="10" viewBox="0 0 10 10"><rect width="10" height="10" fill="#fff"/><path d="M5 1.5C3.3 1.5 2.3 2.7 2.3 4c0 2 2.7 4.5 2.7 4.5S7.7 6 7.7 4c0-1.3-1-2.5-2.7-2.5z" fill="var(--brand-blue)"/></svg>
    <p>7215 Pellham Avenue, Suite 4B<br>Linden Harbor, N.Y. 11592, USA</p>
  </div>
</section>

<section class="sheet envelope-back" aria-label="Envelope back">
  <div class="flap"></div>
</section>

<section class="card card-front" aria-label="Business card front">
  <div class="identity">
    <div class="brand-mark"><span class="square"></span>Valdora</div>
    <p class="person-name">Marcus Valdora</p>
    <p class="person-role">President</p>
  </div>
  <div class="details">
    <div>
      <p><span class="dot"></span>Marc.valdora</p>
      <p><span class="dot"></span>555.382.6047</p>
      <p><span class="dot"></span>7215 Pellham Avenue<br>Suite 4B, Linden Harbor<br>N.Y. 11592, USA</p>
    </div>
    <div>
      <p><span class="dot"></span>www.valdorapartners.com</p>
      <p><span class="dot"></span>Mvaldora@valdorapartners.com</p>
    </div>
  </div>
</section>

<section class="card card-back" aria-label="Business card back">
  <div class="brand-mark"><span class="square"></span>Valdora</div>
</section>

<h1 class="presentation-title">VALDORAPARTNERS</h1>

</body>
</html>
```